Australian residential property business needs a business card design

I need a business card design for my new business 'Meadow Estate Partners'. The business will involve house purchases, land development sites, renovation projects, sub-divisions etc. I will be buying property from motivated vendors and working with property investors. I will deal with a wide range of people working in the residential property market including real estate agents, councils, tradespeople, banks, home owners, etc.

I would like something simple, not flashy, but a little bit unique. The colours should be in line with my logo. The business card needs to be professional. I would like something memorable, but not 'busy' or too bright. Not boring. Modern ok.

Target Market(s)

Home owners looking to sell their property, real estate agents, tradespeople (e.g. plumbers, builders, electricians etc), property investors, local councils, and anyone else involved in the residential property industry

Industry/Entity Type

Business

Contact Information for Business Card

I need to include my business name/logo, my name, my title, a PO Box number/address, a mobile number, and an email address.

Font styles to use
Serif

Requirements
Must have
• My business card details listed above.

```html
<!DOCTYPE html>
<html lang="en">
<head>
<meta charset="utf-8">
<title>Meadow Estate Partners – Business Card</title>
<link rel="stylesheet" href="https://fonts.googleapis.com/css2?family=PT+Sans:wght@400;700&display=swap">
<style>
  :root {
    --page-bg: #e9e6e1;
    --card-green-light: #2a8a52;
    --card-green: #16703a;
    --card-green-dark: #0d5a2b;
    --accent-orange: #e08a2e;
    --text-dark: #233a2c;
    --panel-light: #ece9e4;
    --panel-mid: #cfcac3;
  }
  * { margin: 0; padding: 0; box-sizing: border-box; }
  html, body {
    width: 1200px;
    height: 970px;
    overflow: hidden;
    background: var(--page-bg);
    font-family: "PT Sans", "Helvetica Neue", Arial, sans-serif;
  }
  .business-card {
    position: absolute;
    left: 100px;
    top: 208px;
    width: 1000px;
    height: 553px;
    background: linear-gradient(100deg, var(--card-green-light) 0%, var(--card-green) 45%, var(--card-green-dark) 100%);
    overflow: hidden;
    box-shadow: 0 10px 30px rgba(0,0,0,0.18);
  }
  .company-name {
    position: absolute;
    left: 48px;
    top: 76px;
    font-size: 32px;
    color: var(--accent-orange);
    font-weight: 400;
    line-height: 1.2;
  }
  .person-name {
    position: absolute;
    left: 48px;
    top: 196px;
    font-size: 39px;
    color: var(--accent-orange);
    line-height: 1;
  }
  .person-title {
    position: absolute;
    left: 48px;
    top: 240px;
    font-size: 23px;
    color: var(--text-dark);
  }
  .address {
    position: absolute;
    left: 48px;
    top: 320px;
    font-size: 24px;
    line-height: 33px;
    color: var(--text-dark);
    font-style: normal;
  }
  .contact-list {
    position: absolute;
    left: 48px;
    top: 436px;
    list-style: none;
    font-size: 24px;
    line-height: 33px;
    color: var(--text-dark);
  }
  .contact-list li { display: flex; align-items: center; gap: 12px; }
  .contact-icon { width: 22px; height: 22px; flex: none; }
  .map-placeholder {
    position: absolute;
    left: 517px;
    top: 237px;
    width: 483px;
    height: 316px;
    background: linear-gradient(135deg, var(--panel-light) 0%, var(--panel-mid) 100%);
    border-top-left-radius: 24px;
  }
  .brand-lockup {
    position: absolute;
    left: 517px;
    top: 396px;
    width: 483px;
    display: flex;
    justify-content: center;
    align-items: center;
    gap: 12px;
  }
  .brand-mark {
    width: 20px;
    height: 20px;
    border-radius: 50%;
    background: var(--accent-orange);
  }
  .brand-name {
    font-size: 27px;
    font-weight: 400;
    color: var(--accent-orange);
    letter-spacing: 1px;
    text-transform: uppercase;
  }
</style>
</head>
<body>
  <main class="business-card">
    <h1 class="company-name">Meadow Estate Partners</h1>

    <p class="person-name">Liam Ashford</p>
    <p class="person-title">Director</p>

    <address class="address">
      4120 Harlow Lane<br>
      Brookfield, KS 66010
    </address>

    <ul class="contact-list">
      <li>
        <svg class="contact-icon" viewBox="0 0 22 22" aria-hidden="true">
          <rect x="6" y="2" width="10" height="18" rx="2" fill="none" stroke="var(--accent-orange)" stroke-width="2"/>
          <circle cx="11" cy="16.5" r="1.2" fill="var(--accent-orange)"/>
        </svg>
        <span>555 210 3388</span>
      </li>
      <li>
        <svg class="contact-icon" viewBox="0 0 22 22" aria-hidden="true">
          <rect x="2" y="5" width="18" height="13" fill="var(--accent-orange)"/>
          <path d="M2 5 L11 12 L20 5" fill="none" stroke="var(--card-green)" stroke-width="1.6"/>
        </svg>
        <span>hello@meadowestate.com</span>
      </li>
    </ul>

    <div class="map-placeholder" role="img" aria-label="Pale map silhouette of the home country behind the brand name"></div>

    <div class="brand-lockup">
      <span class="brand-mark" aria-hidden="true"></span>
      <span class="brand-name">Meadow Estate Partners</span>
    </div>
  </main>
</body>
</html>
```